Bring Days 4 Wonder campaign: promoting kids play in the UK - Website Redesign

Bring Days 4 Wonder is a national UK campaign that promotes the value of play for children. The current website is live at http://www.bringdays4wonder.co.uk. This website has been live for 4 years and now needs to be redesigned. The target audience is parents of young children up to the age of 12.

The current site was designed with a series of old adverts in mind. Here is an example of an old advert: http://vidshare.example/k3RwqLmZ8Tb

Criticisms of existing site:
The design represented the adverts too closely. The result was a website that mirrors the adverts rather than complements them.
The color scheme is too dark.
Text-heavy pages (e.g. http://www.bringdays4wonder.co.uk/fun.php) are dull and not FUN!

New site
We have recently had a series of new video adverts produced:
advert 1: http://vidshare.example/Hq2vXnB7eJs
advert 2: http://vidshare.example/Wm9cTpR4uLd
advert 3: http://vidshare.example/Zg5sKbN1oVe

The new site should be cleaner and brighter than the existing site, possibly with a white background using graphics, fonts and advert characters (see attached character graphics files) to add the element of fun and play.

The homepage should include:
1. Bring Days for Wonder logo (attached)
2. Social Media links (visible on all pages of the site) – Friendbook, Chirper, VidShare
3. Link to the BringDays4Wonder app page of the site (visible on all pages)
4. Image/video placeholder that the user can scroll through, view full-size images and play videos.
5. Text area to hold approximately 100 words describing the purpose of the campaign
6. Site footer to contain the same information as on the existing site along with the Northern Game & Craft Guild logo (attached)

Site structure:
One change to the site structure… the “Brought to you by” menu item will be removed from the top-level menu.

General:
Some pages on the existing site are quite text-heavy, we would like to break up text on these pages in some way. Graphical division of paragraphs, use of advert characters?

Please note that all attached graphics file are the property of the Northern Game & Craft Guild and must only be used for the purpose of this project.

```html
<!DOCTYPE html>
<html lang="en">
<head>
<meta charset="utf-8">
<title>Bring Days 4 Wonder</title>
<link href="https://fonts.googleapis.com/css2?family=Oxygen:wght@400;700&family=Courier+Prime:wght@700&display=swap" rel="stylesheet">
<style>
:root{
  --ink:#3a3a55;
  --text:#555;
  --navy:#3d3b66;
  --footer:#3a3a52;
  --card:#ebe8e0;
  --amber:#f0a30a;
  --green:#8cc63f;
  --red:#d8202f;
  --maroon:#b01c1c;
  --yellow:#ffd21f;
  --blue:#3b5998;
  --sky:#1da1f2;
  --tube:#d71e1e;
  --rss:#f7931e;
}
*{box-sizing:border-box;margin:0;padding:0}
html,body{width:1200px;height:2270px;overflow:hidden}
body{position:relative;background:#fff;font-family:"Oxygen",sans-serif;color:var(--text)}
.abs{position:absolute}
.rainbow{left:0;top:0;width:1200px;height:4px;background:linear-gradient(90deg,#e53935,#fbc02d,#8bc34a,#29b6f6,#ab47bc,#e53935)}
.brand{left:174px;top:24px;font-weight:700;font-size:30px;line-height:30px;color:var(--navy);display:flex;align-items:center;gap:10px}
.brand-dot{width:26px;height:26px;border-radius:50%;background:var(--green)}
.brand small{display:block;font-size:14px;font-weight:400}
.social-top{left:930px;top:15px;display:flex;gap:6px}
.social-top span{width:26px;height:26px;border-radius:3px}
.contact-top{right:180px;top:50px;text-align:right;font-size:13px;line-height:22px;color:var(--ink);font-weight:700}
.contact-top em{font-style:normal;color:var(--red)}
.contact-top i{font-style:normal;color:var(--green);font-weight:400}
.thumb-tab{left:1165px;top:30px;width:35px;height:38px;background:var(--green)}
.side-social{left:1150px;top:227px;width:50px}
.side-social span{display:block;width:50px;height:40px}
.hero-bg{left:0;top:106px;width:1200px;height:436px;background:linear-gradient(180deg,#8fd3f0 0%,#c5eaf8 55%,#9ccf4a 72%,#6faf2c 100%)}
.nav{left:174px;top:106px;width:852px;height:48px;background:var(--navy);display:flex;justify-content:space-around;align-items:center;font-family:"Courier Prime",monospace;font-weight:700;font-size:16px}
.hero{left:174px;top:154px;width:852px;height:388px;background:linear-gradient(180deg,#5a8c3a 0%,#9cbf5a 40%,#e8c27a 75%,#f0d59a 100%)}
.hero-arrow{top:282px;width:46px;height:46px;border-radius:50%;background:rgba(255,255,255,.55)}
.tagline{left:372px;top:506px;height:30px;display:flex;align-items:center;gap:12px;font-weight:700;font-size:16px;color:var(--ink)}
.join{background:var(--navy);color:#fff;font-size:13px;padding:6px 14px;border-radius:3px}
.features{left:174px;top:575px;display:flex;gap:12px}
.feature{position:relative;width:161px;height:266px}
.feature .panel{position:absolute;left:0;top:41px;width:161px;height:225px;background:var(--card);text-align:center;padding-top:48px}
.feature.active .panel{background:var(--amber)}
.feature .icon{position:absolute;left:44px;top:0;width:72px;height:72px;border-radius:50%;background:#fff;box-shadow:0 2px 4px rgba(0,0,0,.15);display:flex;align-items:center;justify-content:center}
.feature h3{font-size:13px;font-weight:400;color:var(--ink);line-height:16px}
.feature h3 b{display:block;font-size:20px;line-height:24px}
.feature p{font-size:12.5px;line-height:18px;color:var(--ink);margin:10px 12px 0}
.feature .go{position:absolute;left:68px;bottom:16px;width:26px;height:26px;border-radius:50%;background:#fff;box-shadow:0 1px 3px rgba(0,0,0,.2)}
.round-arrow{width:38px;height:38px;border-radius:50%;background:#fff;box-shadow:0 1px 4px rgba(0,0,0,.25);display:flex;align-items:center;justify-content:center}
.divider{left:0;width:1200px;height:14px}
.section-title{width:1200px;left:0;text-align:center;font-size:33px;color:var(--ink)}
.aside-label{font-size:14px;color:#999}
.player{background:#222}
.player .bar{position:absolute;left:0;top:0;width:100%;height:22px;background:#1c1c1c;color:#ddd;font-size:11px;line-height:22px;padding-left:8px}
.player .bar span{position:absolute;right:8px;top:0}
.player .screen{position:absolute;left:0;top:22px;right:0;bottom:22px}
.player .ctrl{position:absolute;left:0;bottom:0;width:100%;height:22px;background:#141414}
.about-text{left:604px;top:1000px;width:420px;font-size:12px;line-height:17px}
.about-text p{margin-bottom:14px}
.btn{background:var(--navy);color:#fff;font-weight:700;font-size:13px;border-radius:4px;text-align:center;line-height:27px}
.vid-caption{width:239px;text-align:center;font-size:14px;color:var(--ink)}
.vid-caption em{display:block;font-size:12px;color:var(--maroon);font-weight:700}
.vsep{top:1385px;width:1px;height:215px;background:#e4e4e4}
.campaign{left:185px;top:1618px;width:585px}
.campaign h2{font-size:33px;font-weight:400;color:var(--ink);line-height:38px}
.campaign p{font-size:12px;line-height:16px;margin-top:6px}
.campaign em{display:block;color:var(--maroon);font-weight:700;font-size:12px;margin-top:8px}
.download{left:793px;top:1617px;width:239px;height:149px;background:linear-gradient(180deg,#e8252f,#b5151d);border-radius:6px;color:#fff;overflow:hidden}
.download .device{position:absolute;left:14px;top:16px;width:52px;height:112px;border-radius:8px;background:linear-gradient(160deg,#7ac943,#3a8a1f)}
.download h4{position:absolute;left:78px;top:14px;font-size:24px;line-height:30px;white-space:nowrap}
.download .app{position:absolute;left:78px;top:48px;font-size:12px;line-height:16px;color:var(--yellow);font-weight:700;white-space:nowrap}
.download .desc{position:absolute;left:78px;top:66px;width:150px;font-size:12px;line-height:15px}
.download .cta{position:absolute;left:78px;top:114px;font-size:11px;font-weight:700;color:var(--yellow);text-decoration:underline}
.widget{top:1825px;width:238px;height:184px;border:1px solid #ddd;background:#fff}
.widget .head{height:32px;background:var(--yellow);font-weight:700;font-size:15px;color:var(--ink);line-height:32px;padding-left:8px}
.widget .mini{font-size:11px;color:var(--navy);font-weight:700;padding:8px;display:flex;gap:10px;align-items:center;background:#eef1f7}
.widget .mini span{border:1px solid #aab;border-radius:2px;padding:1px 5px;font-weight:400;background:#fff}
.tabs{display:flex;height:32px;font-weight:700;font-size:14px;line-height:32px}
.tabs .on{background:var(--red);color:#fff;padding:0 10px;width:120px}
.tabs .off{background:var(--yellow);color:var(--ink);padding:0 10px;flex:1}
.faces{display:flex;gap:6px;padding:0 8px}
.faces div{width:38px;font-size:11px;text-align:center;color:var(--ink)}
.faces i{display:block;width:38px;height:34px;background:linear-gradient(135deg,#6b7a99,#c9a77d)}
.feed-row{display:flex;gap:8px;padding:6px 8px;font-size:12px;font-style:italic;color:var(--ink);line-height:15px}
.feed-row i{flex:none;width:52px;height:34px;background:linear-gradient(135deg,#7d9b4a,#c8b07a)}
.footer{left:0;top:2050px;width:1200px;height:220px;background:var(--footer);color:#fff}
.footer .frame{position:absolute;left:174px;top:45px;width:852px;height:125px;border:1px solid #5a5a75}
.footer h5{font-size:13px;font-weight:700;margin-bottom:6px}
.footer ul{list-style:none;font-size:12px;line-height:16px}
.up{left:574px;top:2032px;width:32px;height:32px;border-radius:50%;background:var(--amber);display:flex;align-items:center;justify-content:center}
.copyright{left:0;top:2232px;width:1200px;text-align:center;font-size:12px;color:#ddd}
</style>
</head>
<body>
<div class="abs rainbow"></div>

<header>
  <div class="abs brand"><span class="brand-dot"></span><span>Bring Days<small>4 Wonder</small></span></div>
  <div class="abs social-top">
    <span style="background:var(--blue)" aria-label="Friendbook"></span>
    <span style="background:var(--sky)" aria-label="Chirper"></span>
    <span style="background:var(--tube)" aria-label="VidShare"></span>
  </div>
  <div class="abs contact-top">
    <div>&#9742; CALL : <em>014 752 3390</em></div>
    <div>&#9993; EMAIL : <i>hello@bringdays4wonder.co.uk</i></div>
  </div>
</header>

<div class="abs thumb-tab" aria-label="Like"></div>

<div class="abs hero-bg" role="img" aria-label="Cartoon landscape with sky, clouds, trees and green hills"></div>
<nav class="abs nav">
  <span style="color:var(--yellow)">Play right now</span>
  <span style="color:#a5d84a">Get Involved</span>
  <span style="color:#6fc7f2">Why Play</span>
  <span style="color:#ff5a5f">Fun Forever</span>
  <span style="color:var(--amber)">Resources</span>
  <span style="color:#fff">Contact Us</span>
</nav>
<div class="abs hero" role="img" aria-label="Illustration of five cartoon children holding hands in front of a wooden treehouse"></div>
<div class="abs hero-arrow" style="left:188px"></div>
<div class="abs hero-arrow" style="left:966px"></div>
<div class="abs tagline">WE ENTER TO LEARN, LEAVE TO ACHIEVE <span class="join">JOIN US</span></div>

<div class="abs side-social">
  <span style="background:var(--blue)"></span>
  <span style="background:var(--sky)"></span>
  <span style="background:var(--tube)"></span>
  <span style="background:var(--rss)"></span>
</div>

<section class="abs features">
  <div class="feature"><div class="panel"><h3>TREASURE<b>HUNT</b></h3><p>Lorem ipsum dolor sit amet, consectetuer adipiscing elit, sed diam ummy nibh ...</p><span class="go"></span></div>
    <div class="icon"><svg width="40" height="36"><rect x="4" y="12" width="32" height="22" rx="2" fill="#8cc63f"/><path d="M4 14 Q20 -2 36 14Z" fill="#7ab52f"/><rect x="17" y="16" width="6" height="7" fill="#fff"/></svg></div></div>
  <div class="feature"><div class="panel"><h3>EXPAND<b>OUR MIND</b></h3><p>Lorem ipsum dolor sit amet, consectetuer adipiscing elit, sed diam ummy nibh ...</p><span class="go"></span></div>
    <div class="icon"><svg width="42" height="36"><ellipse cx="21" cy="18" rx="19" ry="16" fill="none" stroke="#8cc63f" stroke-width="4"/><line x1="21" y1="3" x2="21" y2="33" stroke="#8cc63f" stroke-width="3"/></svg></div></div>
  <div class="feature active"><div class="panel"><h3>LEARN<b>ABOUT RISK</b></h3><p>Lorem ipsum dolor sit amet, consectetuer adipiscing elit, sed diam ummy nibh ...</p><span class="go"></span></div>
    <div class="icon"><svg width="44" height="40"><path d="M22 3 L41 37 H3Z" fill="none" stroke="#1e88e5" stroke-width="4" stroke-linejoin="round"/><rect x="20" y="14" width="4" height="12" fill="#1e88e5"/><rect x="20" y="29" width="4" height="4" fill="#1e88e5"/></svg></div></div>
  <div class="feature"><div class="panel"><h3>PLAY<b>TOGETHER</b></h3><p>Lorem ipsum dolor sit amet, consectetuer adipiscing elit, sed diam ummy nibh ...</p><span class="go"></span></div>
    <div class="icon"><svg width="40" height="40"><line x1="8" y1="2" x2="24" y2="30" stroke="#8cc63f" stroke-width="3"/><circle cx="14" cy="8" r="5" fill="#8cc63f"/><rect x="18" y="28" width="16" height="5" fill="#8cc63f"/></svg></div></div>
  <div class="feature"><div class="panel"><h3>LEARN<b>TO SHARE</b></h3><p>Lorem ipsum dolor sit amet, consectetuer adipiscing elit, sed diam ummy nibh ...</p><span class="go"></span></div>
    <div class="icon"><svg width="42" height="40"><circle cx="21" cy="8" r="6" fill="#8cc63f"/><circle cx="7" cy="32" r="6" fill="#8cc63f"/><circle cx="35" cy="32" r="6" fill="#8cc63f"/><path d="M21 14 V22 M7 26 V22 H35 V26" stroke="#8cc63f" stroke-width="3" fill="none"/></svg></div></div>
</section>
<div class="abs round-arrow" style="left:114px;top:715px"><svg width="12" height="12"><path d="M8 1 L3 6 L8 11" stroke="#222" stroke-width="2.5" fill="none"/></svg></div>
<div class="abs round-arrow" style="left:1044px;top:715px"><svg width="12" height="12"><path d="M4 1 L9 6 L4 11" stroke="#222" stroke-width="2.5" fill="none"/></svg></div>

<svg class="abs divider" style="top:875px" viewBox="0 0 1200 14" preserveAspectRatio="none"><path d="M0 7 Q150 2 300 8 T600 6 T900 8 T1200 5" stroke="#ccc" stroke-width="2" fill="none"/></svg>

<section>
  <h2 class="abs section-title" style="top:928px;font-weight:400">Few words about Bring Days 4 Wonder</h2>
  <div class="abs aside-label" style="left:926px;top:942px">What We are</div>
  <svg class="abs" style="left:988px;top:915px" width="55" height="70"><path d="M2 4 Q50 4 48 30 Q46 50 20 58" stroke="#888" stroke-width="2" fill="none"/><path d="M28 50 L18 59 L30 64" stroke="#888" stroke-width="2" fill="none"/></svg>
  <div class="abs player" style="left:174px;top:995px;width:395px;height:221px">
    <div class="bar">New breed of accountants measure<span>Like &nbsp; share &nbsp; More info</span></div>
    <div class="screen" role="img" aria-label="Video still of a campaign ambassador speaking to camera" style="background:linear-gradient(90deg,#c0392b 0%,#d9774a 45%,#c98a6a 60%,#5a3b2c 100%)"></div>
    <div class="ctrl"></div>
  </div>
  <div class="abs about-text">
    <p>Bring Days 4 Wonder Ambassador Dr Helena Marsh explains the importance of engaging children in physical activity and the link with body image. Check out her blog here, read the full report here or check out her top tips here.</p>
    <p>Lorem ipsum dolor sit amet, consectetuer adipiscing elit, sed diam nonummy nibh euismod tincidunt ut laoreet dolore magna aliquam erat volutpat. Ut wisi enim ad minim veniam, dolor sit amet, consectetuer adipiscing elit, sed diam nonummy nibh euismod tincidunt ut laoreet dolore magna aliquam erat volutpat. Ut wisi enim ad minim veniam, dolor sit amet, consectetuer adipiscing elit, sed diam nonummy nibh euismod tincidun.</p>
  </div>
  <div class="abs btn" style="left:604px;top:1177px;width:112px">READ MORE</div>
</section>

<svg class="abs divider" style="top:1250px" viewBox="0 0 1200 14" preserveAspectRatio="none"><path d="M0 6 Q200 10 400 5 T800 7 T1200 6" stroke="#ccc" stroke-width="2" fill="none"/></svg>

<section>
  <h2 class="abs section-title" style="top:1302px;font-weight:400">View Play Videos</h2>
  <div class="abs aside-label" style="left:932px;top:1337px">All Videos</div>
  <svg class="abs" style="left:984px;top:1310px" width="55" height="75"><path d="M2 4 Q50 4 48 32 Q46 55 20 64" stroke="#888" stroke-width="2" fill="none"/><path d="M28 56 L18 65 L30 70" stroke="#888" stroke-width="2" fill="none"/></svg>

  <div class="abs player" style="left:185px;top:1398px;width:239px;height:133px">
    <div class="bar" style="font-size:8px;height:14px;line-height:14px">New breed of accountants measure</div>
    <div class="screen" style="top:14px;bottom:12px;background:linear-gradient(180deg,#6e8f3a,#b29a6a)" role="img" aria-label="Parent helping a toddler climb on a wooden box outdoors"></div>
    <div class="ctrl" style="height:12px"></div>
  </div>
  <div class="abs player" style="left:480px;top:1398px;width:237px;height:133px">
    <div class="bar" style="font-size:8px;height:14px;line-height:14px">New breed of accountants measure</div>
    <div class="screen" style="top:14px;bottom:12px;background:linear-gradient(180deg,#d8cfc0,#c36d4a)" role="img" aria-label="Mother and child playing with building blocks on the floor"></div>
    <div class="ctrl" style="height:12px"></div>
  </div>
  <div class="abs player" style="left:779px;top:1398px;width:239px;height:133px">
    <div class="bar" style="font-size:8px;height:14px;line-height:14px">New breed of accountants measure</div>
    <div class="screen" style="top:14px;bottom:12px;background:linear-gradient(180deg,#e9e3d8,#b7634a)" role="img" aria-label="Children playing together at a nursery table"></div>
    <div class="ctrl" style="height:12px"></div>
  </div>
  <div class="abs vsep" style="left:449px"></div>
  <div class="abs vsep" style="left:747px"></div>
  <div class="abs vid-caption" style="left:185px;top:1541px">How far I can go?<em>- read more</em></div>
  <div class="abs vid-caption" style="left:479px;top:1541px">Explore the World.<em>- read more</em></div>
  <div class="abs vid-caption" style="left:779px;top:1541px">Learn about risks.<em>- read more</em></div>
  <div class="abs round-arrow" style="left:114px;top:1509px"><svg width="12" height="12"><path d="M8 1 L3 6 L8 11" stroke="#222" stroke-width="2.5" fill="none"/></svg></div>
  <div class="abs round-arrow" style="left:1048px;top:1453px"><svg width="12" height="12"><path d="M4 1 L9 6 L4 11" stroke="#222" stroke-width="2.5" fill="none"/></svg></div>
</section>

<section class="abs campaign">
  <h2>Campaign Purpose</h2>
  <p>Lorem ipsum dolor sit amet, consectetuer adipiscing elit, sed diam nonummy nibh euismod tincidunt ut laoreet dolore magna aliquam erat volutpat. Ut wisi enim ad minim veniam, Sed ut perspiciatis unde omnis iste natus error sit voluptatem accusantium doloremque laudantium, totam rem aperiam, eaque ipsa quae ab illo inven tore veritatis et quasi architecto beatae vitae dicta sunt explicabo.</p>
  <p style="margin-top:14px">Nemo enim ipsam voluptatem quia voluptas sit aspernatur aut odit aut fugit, sed quia consequuntur magni dolores eos qui ratione voluptatem sequi nesciunt. Neque porro quisquames.</p>
  <em>- read more</em>
</section>

<div class="abs download">
  <div class="device" role="img" aria-label="Illustration of a green mobile phone"></div>
  <h4>DOWNLOAD</h4>
  <div class="app">BringDays4Wonder App</div>
  <div class="desc">Lorem ipsum dolor sits consectetur adipi</div>
  <div class="cta">CLICK TO DOWNLOAD</div>
</div>

<div class="abs widget" style="left:186px">
  <div class="head">Play Idea Of Our Day</div>
  <div role="img" aria-label="Children playing in a sandpit" style="height:88px;background:linear-gradient(135deg,#c9b48a,#8a6a9a)"></div>
  <div style="font-size:11.5px;line-height:14px;color:var(--ink);padding:4px 8px">Lorem ipsum dolor sit amet, consectetuer Lorem ipsum dolor sit amet, consectetuer Lorem ipsum dolor sit amet</div>
  <div style="position:absolute;right:8px;bottom:4px;font-size:11px;font-style:italic;color:var(--ink)">Read More &gt;</div>
</div>

<div class="abs widget" style="left:478px">
  <div class="tabs"><span class="on">Friends Feed</span><span class="off">Chirp Feed</span></div>
  <div class="mini">Bring Days 4 Wonder <span>Like</span></div>
  <div style="font-size:11px;font-weight:700;color:var(--ink);padding:6px 8px">3,612 people like BringDays4Wonder.co.uk</div>
  <div class="faces">
    <div><i></i>Theo</div><div><i></i>Mira</div><div><i></i>Ollie</div><div><i></i>Juno</div><div><i></i>Theo</div>
  </div>
</div>

<div class="abs widget" style="left:781px">
  <div class="head">Video Feed</div>
  <div class="mini">Bring Days 4 Wonder <span>Like</span></div>
  <div class="feed-row"><i role="img" aria-label="Video thumbnail"></i>Lorem ipsum dolor sit amet consectetuer</div>
  <div class="feed-row"><i role="img" aria-label="Video thumbnail"></i>Lorem ipsum dolor sit amet consectetuer</div>
  <div style="position:absolute;right:8px;bottom:4px;font-size:11px;color:var(--ink)">View All &gt;</div>
</div>

<footer class="abs footer">
  <div class="frame">
    <div style="position:absolute;left:33px;top:14px"><h5>Quick Links</h5>
      <ul><li>Play Right Now</li><li>Get Unvolved</li><li>Why Play</li><li>Fun Forever</li><li>Resources</li><li>Contact Us</li></ul></div>
    <div style="position:absolute;left:157px;top:14px"><h5>Contact Us</h5>
      <ul><li>Street no., Street name, City,</li><li>State, Country. Zip Code.</li></ul>
      <div style="font-size:12px;margin-top:14px">&#9742; &nbsp;014-752-3390</div>
      <div style="font-size:12px;margin-top:14px">&#9743; &nbsp;014-752-3390</div></div>
    <div style="position:absolute;right:100px;top:22px;text-align:right;font-size:14px;line-height:18px">
      <div style="font-weight:700;font-size:16px">© 2014 Northern Game &amp; Craft Guild Ltd.</div>
      <div>14 Harrow Lane, Leeds, LS2 7QA</div>
      <div style="font-size:12px">Click here to read the disclaimer</div></div>
    <div style="position:absolute;right:20px;top:22px;width:66px;height:66px;background:#fff;border-radius:4px"></div>
  </div>
</footer>
<div class="abs up"><svg width="14" height="10"><path d="M1 9 L7 3 L13 9" stroke="#fff" stroke-width="2.5" fill="none"/></svg></div>
<div class="abs copyright">Copyright © 2014. BringDays4Wonder. All Rights Reserved.</div>
</body>
</html>
```